Acupuncture Medspa needs a business card design

I need a business card design that looks professional, has a spa-like quality and can offer a promo on the back. Initial promo is "First session free". The tagline of NeedleNook is: Refresh, Restore, Rejuvenate.

NeedleNook is a membership-based acupuncture medspa that offers acupuncture, cupping, and herbal therapies. Members choose between the "Refresh" membership which is for stress relief, or "Restore" which is for treating health conditions, and lastly "Rejuvenate" which is for natural facial enhancement.

Industry/Entity Type

Health And Wellness

Contact Information for Business Card

Coral Haskins, MAC, L.Ac.
612-555-0193
www.needlenook-example.com

Font styles to use
Serif
Sans Serif

Colors

Designer to choose colors to be used in the design.

Requirements
Must have
• The project must have NeedleNook logo, promo on the back, and contact information
Nice to have
• I would like to see the colors of the logo used.

```html
<!DOCTYPE html>
<html lang="en">
<head>
<meta charset="UTF-8">
<title>NeedleNook Business Card</title>
<link href="https://fonts.googleapis.com/css2?family=Roboto:wght@400;500&family=Roboto+Condensed:wght@700&display=swap" rel="stylesheet">
<style>
  :root {
    --teal: #17958a;
    --teal-deep: #0f8277;
    --teal-soft: #3aa99f;
    --ink: #2b2b2b;
    --grey: #555;
    --paper: #ffffff;
    --stage: #3b3b3d;
  }
  html, body {
    margin: 0;
    padding: 0;
    width: 1200px;
    height: 900px;
    overflow: hidden;
    background: var(--stage);
    font-family: "Roboto", Arial, sans-serif;
  }
  .canvas {
    position: relative;
    width: 1200px;
    height: 900px;
  }
  .card {
    position: absolute;
    left: 250px;
    width: 700px;
    height: 400px;
    border-radius: 28px;
    overflow: hidden;
    box-shadow: 0 12px 30px rgba(0,0,0,0.35);
  }
  /* Back */
  .card-back {
    top: 35px;
    background: var(--teal);
  }
  .back-pattern {
    position: absolute;
    inset: 0;
    background: radial-gradient(circle at 40% 40%, var(--teal-soft), var(--teal) 70%);
  }
  .promo {
    position: absolute;
    left: 0;
    right: 0;
    top: 165px;
    text-align: center;
    color: var(--paper);
  }
  .promo-title {
    font-size: 34px;
    font-weight: 400;
    letter-spacing: 0.5px;
    margin: 0;
  }
  .promo-tagline {
    font-size: 20px;
    margin: 8px 0 0;
    opacity: 0.95;
  }
  /* Front */
  .card-front {
    top: 465px;
    background: var(--paper);
  }
  .brand {
    position: absolute;
    left: 45px;
    top: 105px;
  }
  .brand-name {
    display: flex;
    align-items: center;
    gap: 10px;
    color: var(--teal);
    font-size: 46px;
    font-weight: 500;
    letter-spacing: 1px;
    margin: 0;
  }
  .brand-dot {
    width: 14px;
    height: 14px;
    border-radius: 50%;
    background: var(--teal);
  }
  .brand-tagline {
    margin: 4px 0 0 2px;
    color: var(--grey);
    font-size: 19px;
    letter-spacing: 0.5px;
  }
  .brand-mark {
    position: absolute;
    right: 40px;
    top: 45px;
    width: 300px;
    height: 300px;
  }
  .person {
    position: absolute;
    left: 45px;
    top: 245px;
  }
  .person-name {
    margin: 0;
    font-family: "Roboto Condensed", "Arial Narrow", sans-serif;
    font-weight: 700;
    font-size: 24px;
    color: var(--teal);
  }
  .person-role {
    margin: 2px 0 0;
    font-size: 16px;
    color: var(--ink);
  }
  .contact {
    position: absolute;
    left: 45px;
    top: 318px;
    margin: 0;
    padding: 0;
    list-style: none;
    font-size: 14px;
    color: var(--ink);
  }
  .contact li {
    display: flex;
    align-items: center;
    gap: 10px;
    height: 22px;
  }
  .contact svg {
    width: 14px;
    height: 14px;
    fill: none;
    stroke: var(--teal);
    stroke-width: 2;
  }
</style>
</head>
<body>
<div class="canvas">

  <section class="card card-back">
    <div class="back-pattern" role="img" aria-label="Repeating pattern of the NeedleNook brand symbol in soft teal tones"></div>
    <div class="promo">
      <p class="promo-title">First Session Free</p>
      <p class="promo-tagline">Refresh &bull; Restore &bull; Rejuvenate</p>
    </div>
  </section>

  <section class="card card-front">
    <div class="brand">
      <p class="brand-name">NeedleNook <span class="brand-dot"></span></p>
      <p class="brand-tagline">Refresh &bull; Restore &bull; Rejuvenate</p>
    </div>

    <svg class="brand-mark" viewBox="0 0 300 300" aria-hidden="true">
      <circle cx="150" cy="150" r="138" fill="none" stroke="var(--teal)" stroke-width="8"/>
    </svg>

    <div class="person">
      <p class="person-name">Coral Haskins, MAC, L.Ac.</p>
      <p class="person-role">President</p>
    </div>

    <ul class="contact">
      <li>
        <svg viewBox="0 0 24 24"><path d="M5 3h4l2 5-3 2a12 12 0 0 0 6 6l2-3 5 2v4a2 2 0 0 1-2 2A17 17 0 0 1 3 5a2 2 0 0 1 2-2z"/></svg>
        612-555-0193
      </li>
      <li>
        <svg viewBox="0 0 24 24"><rect x="2" y="5" width="20" height="14" rx="1"/><path d="M2 6l10 7 10-7"/></svg>
        coral@needlenook-example.com
      </li>
      <li>
        <svg viewBox="0 0 24 24"><circle cx="12" cy="12" r="10"/><path d="M2 12h20M12 2a15 15 0 0 1 0 20M12 2a15 15 0 0 0 0 20"/></svg>
        www.needlenook-example.com
      </li>
    </ul>
  </section>

</div>
</body>
</html>
```